3 Sympathy Cards for Veterinary Hospital

Hi. Brookvale Pet Hospital is a Veterinary Hospital in Australia. We need sympathy cards to send to grieving clients after the loss of their beloved pets.
I have attached the old designs, but we have rebranded and need something to suit our new image.

The cards should have a nice message and appeal to every owner.
They need to match our current branding, but the cards are for the clients, not to advertise us, so not too much branding.
The current cards are attached and they are good because they show a variety of animals so clients might identify with one of them.
I have attached a brown to green gradient that we use on some designs, you don't have to use it, but consider it.
I have attached a logo on background used in some of our new designs, consider using it.
I have attached a font that we use for most new branding.

Target Market(s)

Women 25 to 44

Industry/Entity Type

Veterinary

Font styles to use
Sans Serif
Script

Colors
fac994
cadf82

Requirements
Must have
• IMPORTANT - 3 different designs for the different types of pets.
• 1. Dog.
• 2. Cat.
• 3. Everything else (Rabbits, lizards, ferrets, chickens, birds, mice, rats, snakes)
Nice to have
• Caring and compassionate message.
Should not have
• Too much branding.

```html
<!DOCTYPE html>
<html lang="en">
<head>
<meta charset="utf-8">
<title>Brookvale Pet Hospital – Sympathy Cards</title>
<link rel="stylesheet" href="https://fonts.googleapis.com/css2?family=Parisienne&family=Open+Sans:wght@400;700&display=swap">
<style>
:root{
  --stage:#3b3b31;
  --orange:#fac994;
  --green:#cadf82;
  --cream:#fdebd2;
  --mint:#e5efc9;
  --ink:#4a2718;
  --heart:#d3242b;
  --logo-panel:#f7f1e2;
}
*{margin:0;padding:0;box-sizing:border-box}
html,body{width:1200px;height:1045px;overflow:hidden;background:var(--stage)}
.stage{position:relative;width:1200px;height:1045px}
.card{position:absolute;top:135px;width:353px;height:546px;background:var(--cream);overflow:hidden}
.card--cat{left:46px}
.card--dog{left:426px;background:var(--mint)}
.card--small{left:800px}
.card__band{position:absolute;left:0;top:0;width:100%;height:13px;background:var(--green)}
.card__rule{position:absolute;left:0;top:13px;width:100%;height:6px;background:var(--orange)}
.card__back{position:absolute;left:0;top:22px;width:100%;transform:rotate(180deg);text-align:center;
  font-family:"Open Sans",sans-serif;color:var(--ink)}
.card__copyright{font-size:6px;line-height:9px;font-weight:400}
.brand{display:inline-block;margin-bottom:4px;width:100px;height:90px;background:var(--logo-panel);
  padding-top:30px;font-size:11px;font-weight:700;line-height:14px;letter-spacing:.5px;color:var(--ink)}
.block,.photo{position:absolute}
.block--orange{background:var(--orange)}
.block--green{background:var(--green)}
.photo{box-shadow:0 1px 3px rgba(0,0,0,.25)}
.message{position:absolute;right:18px;text-align:right;font-family:"Parisienne",cursive;color:var(--ink);white-space:nowrap}
.message--large{top:436px;font-size:27px;line-height:31px}
.message--small{font-size:17px;line-height:22px}
.heart{display:inline-block;vertical-align:middle;margin-right:4px}
</style>
</head>
<body>
<div class="stage">

  <section class="card card--cat" aria-label="Cat sympathy card">
    <div class="card__band"></div><div class="card__rule"></div>
    <div class="card__back">
      <div class="brand">BROOKVALE PET<br>HOSPITAL</div>
      <p class="card__copyright">Copyright 2017 Brookvale Card Supplies<br>PO Box 12, Brookvale 2100 Ph 1300 000 000</p>
    </div>
    <div class="block block--orange" style="left:0;top:276px;width:111px;height:20px"></div>
    <div class="block block--green" style="left:111px;top:276px;width:128px;height:31px"></div>
    <div class="block block--orange" style="left:0;top:379px;width:111px;height:21px"></div>
    <div class="block block--orange" style="left:243px;top:366px;width:110px;height:65px"></div>
    <div class="photo" role="img" aria-label="Photo of a grey and white cat" style="left:1px;top:296px;width:110px;height:83px;background:linear-gradient(135deg,#8d8d88,#e6e4de 55%,#b5b2aa)"></div>
    <div class="photo" role="img" aria-label="Photo of a ginger and white cat" style="left:111px;top:303px;width:128px;height:95px;background:linear-gradient(120deg,#b9854a,#f1e3c9 60%,#c99a5e)"></div>
    <div class="photo" role="img" aria-label="Photo of a silver tabby cat lying down" style="left:243px;top:282px;width:107px;height:84px;background:linear-gradient(135deg,#f4f4f4,#a9a9a6 60%,#d8d8d6)"></div>
    <p class="message message--large">You remember always<br><svg class="heart" width="22" height="19" viewBox="0 0 22 19"><path d="M11 19 1.6 9.6A5.5 5.5 0 0 1 11 2.2a5.5 5.5 0 0 1 9.4 7.4Z" fill="var(--heart)"/></svg>make us smile...</p>
  </section>

  <section class="card card--dog" aria-label="Dog sympathy card">
    <div class="card__band"></div><div class="card__rule"></div>
    <div class="card__back">
      <div class="brand">BROOKVALE PET<br>HOSPITAL</div>
      <p class="card__copyright">Copyright 2017 Brookvale Card Supplies<br>PO Box 12, Brookvale 2100 Ph 1300 000 000</p>
    </div>
    <div class="block block--orange" style="left:113px;top:396px;width:128px;height:66px"></div>
    <div class="photo" role="img" aria-label="Photo of a golden spaniel sitting outdoors" style="left:0;top:276px;width:113px;height:138px;background:linear-gradient(160deg,#6d7b4a,#b5742f 55%,#8a5124)"></div>
    <div class="photo" role="img" aria-label="Photo of a child with a large white dog" style="left:113px;top:279px;width:128px;height:117px;background:linear-gradient(135deg,#8c8b7a,#efeee8 55%,#c9c8bf)"></div>
    <div class="photo" role="img" aria-label="Photo of a black puppy beside boots" style="left:241px;top:276px;width:112px;height:155px;background:linear-gradient(180deg,#4d5a66,#1e1e22 55%,#7a4a2c)"></div>
    <p class="message message--small" style="top:477px">One day I need a helping hand, and I got a paw.<br><svg class="heart" width="16" height="14" viewBox="0 0 22 19"><path d="M11 19 1.6 9.6A5.5 5.5 0 0 1 11 2.2a5.5 5.5 0 0 1 9.4 7.4Z" fill="var(--heart)"/></svg>I'll always remember you.</p>
  </section>

  <section class="card card--small" aria-label="Small pets sympathy card">
    <div class="card__band"></div><div class="card__rule"></div>
    <div class="card__back">
      <div class="brand">BROOKVALE PET<br>HOSPITAL</div>
      <p class="card__copyright">Copyright 2017 Brookvale Card Supplies<br>PO Box 12, Brookvale 2100 Ph 1300 000 000</p>
    </div>
    <div class="block block--green" style="left:0;top:390px;width:108px;height:33px"></div>
    <div class="block block--orange" style="left:239px;top:390px;width:114px;height:20px"></div>
    <div class="photo" role="img" aria-label="Photo of rabbits and chicks" style="left:0;top:272px;width:108px;height:67px;background:linear-gradient(135deg,#5f7a3a,#e9e2d3 55%,#9a8a5a)"></div>
    <div class="photo" role="img" aria-label="Photo of a ferret" style="left:108px;top:272px;width:125px;height:67px;background:linear-gradient(135deg,#3d3a34,#9c9486 55%,#5a5246)"></div>
    <div class="photo" role="img" aria-label="Photo of a pet rat" style="left:233px;top:272px;width:120px;height:67px;background:linear-gradient(135deg,#7a8a4a,#6a4a3a 50%,#e8d8d0)"></div>
    <div class="photo" role="img" aria-label="Photo of a lizard" style="left:0;top:339px;width:108px;height:62px;background:linear-gradient(135deg,#3e4a2a,#c9a23a 55%,#5a5a3a)"></div>
    <div class="photo" role="img" aria-label="Photo of a small lizard held in a hand" style="left:108px;top:339px;width:125px;height:94px;background:linear-gradient(135deg,#c7a17a,#e7c29a 50%,#a77a52)"></div>
    <div class="photo" role="img" aria-label="Photo of a turtle on a log" style="left:233px;top:339px;width:120px;height:72px;background:linear-gradient(180deg,#6f7a4a,#3a3a2a 55%,#9a8a6a)"></div>
    <p class="message message--small" style="top:470px"><svg class="heart" width="16" height="14" viewBox="0 0 22 19"><path d="M11 19 1.6 9.6A5.5 5.5 0 0 1 11 2.2a5.5 5.5 0 0 1 9.4 7.4Z" fill="var(--heart)"/></svg>A pet leaves footprints forever in your heart</p>
  </section>

</div>
</body>
</html>
```